New Business Card Design*

We are a recruitment company based in Norwich/Cambridge England.
I have included our company logo which we want to remain the same.

What we are looking for is a new creative Business card which will really stand out!!

Contact Information for Business Card

Harriet Vance
email: Harriet@brelvix.co.uk
Address: Tolworth House
Ashgrove Innovation Park
Pelham Road
Norwich
KT9 3QD
Tel:01632 960418

```html
<!DOCTYPE html>
<html lang="en">
<head>
<meta charset="utf-8">
<title>Brelvix Business Card</title>
<link rel="stylesheet" href="https://fonts.googleapis.com/css2?family=Lato:wght@400;700&family=Roboto:wght@400&display=swap">
<style>
  :root {
    --backdrop: #262626;
    --card-white: #f3f3f3;
    --brand-green: #84bd3a;
    --text-grey: #555555;
    --title-grey: #8a8a8a;
    --rule-grey: #9a9a9a;
    --logo-grey: #7d7d80;
    --white: #ffffff;
  }
  * { margin: 0; padding: 0; box-sizing: border-box; }
  html, body {
    width: 1200px; height: 960px; overflow: hidden;
    background: var(--backdrop);
    font-family: "Lato", sans-serif;
  }
  .stage { position: relative; width: 1200px; height: 960px; }

  .card {
    position: absolute;
    width: 600px; height: 342px;
    border-radius: 22px;
    overflow: hidden;
  }
  .card-front { left: 314px; top: 113px; background: var(--card-white); }
  .card-back  { left: 311px; top: 472px; background: var(--brand-green); }

  /* Front: brand */
  .brand {
    position: absolute; right: 48px; top: 46px;
    display: flex; align-items: center; gap: 14px;
  }
  .brand-dot { width: 46px; height: 46px; border-radius: 50%; background: var(--logo-grey); }
  .brand-name { font-weight: 700; font-size: 38px; color: var(--brand-green); letter-spacing: -0.5px; }

  /* Front: identity */
  .accent-bar {
    position: absolute; left: 0; top: 151px;
    width: 17px; height: 40px; background: var(--brand-green);
  }
  .person { position: absolute; left: 41px; top: 146px; }
  .person-name {
    font-size: 24px; font-weight: 400; color: var(--brand-green);
    text-transform: uppercase; line-height: 1.05;
  }
  .person-title {
    font-size: 15px; color: var(--title-grey);
    text-transform: uppercase; margin-top: 1px;
  }

  /* Front: contacts */
  .contacts { position: absolute; left: 42px; top: 211px; list-style: none; }
  .contacts li {
    display: flex; align-items: center; gap: 8px;
    height: 19px; font-size: 14.5px; color: var(--text-grey);
  }
  .contacts svg { width: 14px; height: 14px; fill: var(--brand-green); flex: none; }

  .divider {
    position: absolute; left: 212px; top: 273px;
    width: 1px; height: 31px; background: var(--rule-grey);
  }
  .address {
    position: absolute; left: 235px; top: 271px;
    font-style: normal; font-size: 14.5px; line-height: 18px; color: var(--text-grey);
  }

  /* Back */
  .back-brand {
    position: absolute; left: 0; right: 0; top: 110px;
    display: flex; flex-direction: column; align-items: center; gap: 14px;
  }
  .back-dot { width: 64px; height: 64px; border-radius: 50%; background: var(--white); }
  .back-name { font-weight: 700; font-size: 44px; color: var(--white); }
  .back-web {
    position: absolute; left: 0; right: 0; top: 299px; text-align: center;
    font-family: "Roboto", sans-serif; font-size: 14px; letter-spacing: 5px; color: var(--white);
  }
</style>
</head>
<body>
<main class="stage">

  <section class="card card-front" aria-label="Business card front">
    <div class="brand">
      <span class="brand-dot"></span>
      <span class="brand-name">Brelvix</span>
    </div>

    <span class="accent-bar"></span>
    <div class="person">
      <h1 class="person-name">Harriet Vance</h1>
      <p class="person-title">CEO/Founder</p>
    </div>

    <ul class="contacts">
      <li>
        <svg viewBox="0 0 16 16" aria-hidden="true"><path d="M3.6 1.2 6 3.6 4.7 5.6c.9 2 2.6 3.7 4.7 4.7l2-1.3 2.4 2.4-1.6 2.6C7 13.6 2.4 9 1 3.1z"/></svg>
        01632 960418
      </li>
      <li>
        <svg viewBox="0 0 16 16" aria-hidden="true"><path d="M4.5 0h7a1 1 0 0 1 1 1v14a1 1 0 0 1-1 1h-7a1 1 0 0 1-1-1V1a1 1 0 0 1 1-1zm.8 2v10.5h5.4V2zM8 13.3a.9.9 0 1 0 0 1.8.9.9 0 0 0 0-1.8z"/></svg>
        01632 960527
      </li>
      <li>
        <svg viewBox="0 0 16 16" aria-hidden="true"><path d="M4 1h8v4H4zM1 6h14v6h-2.5v-2h-9v2H1zm3.5 5h7v4h-7z"/></svg>
        01632 960733
      </li>
      <li>
        <svg viewBox="0 0 16 16" aria-hidden="true"><path d="M1 3h14v1.2L8 8.6 1 4.2zm0 2.6 7 4.4 7-4.4V13H1z"/></svg>
        harriet@brelvix.co.uk
      </li>
      <li>
        <svg viewBox="0 0 16 16" aria-hidden="true"><path d="M8 1a7 7 0 1 0 0 14A7 7 0 0 0 8 1zm-1 2.3c.5 1-.6 1.6-1.5 2.2-.6.5 0 1.4.9 1.5 1 .1 1.5.9 1.2 1.8-.3.8-1 1.2-.8 2.4.1.8-.8 1.3-1.4.6C4 10.3 3.3 8 3.5 6.3 4.2 4.6 5.5 3.5 7 3.3zm4.3 1.6c1 1 1.6 2.4 1.6 3.9-.6.6-1.5.5-1.8-.3-.3-.9-1.3-1-1.6-1.9-.3-.8.7-1.4 1.8-1.7z"/></svg>
        www.brelvix.co.uk
      </li>
    </ul>

    <span class="divider"></span>
    <address class="address">
      Tolworth House, Pelham Road<br>
      Norwich KT9 3QD
    </address>
  </section>

  <section class="card card-back" aria-label="Business card back">
    <div class="back-brand">
      <span class="back-dot"></span>
      <span class="back-name">Brelvix</span>
    </div>
    <p class="back-web">www.brelvix.co.uk</p>
  </section>

</main>
</body>
</html>
```